Business Card Design Project

Hi

I have a draft of a business card which I need smarting up. I have attached the pdf of this.
The information on the front is correct.
The information on the back should contain:
Project Management, Consulting, Master Systems Integrator, Datacenter, Relocations, Restacks. I want this spiraling around the back

Can you change the telephone number to +65 8476 2153.

Target Market(s)

Chief Technology Officers of large multi-nationals

Industry/Entity Type

Business

Requirements
Must have
• My logo - Vorbelt (attached)
The orange and blue colour running around the edge

```html
<!DOCTYPE html>
<html lang="en">
<head>
<meta charset="utf-8">
<title>Vorbelt Business Card</title>
<link rel="stylesheet" href="https://fonts.googleapis.com/css2?family=Belleza&family=Questrial&display=swap">
<style>
  :root {
    --page: #ffffff;
    --card: #ffffff;
    --card-edge: #d9d9d9;
    --blue: #0fb4f2;
    --blue-light: #18f0f4;
    --orange: #f7931e;
    --orange-light: #fdc51c;
    --ink: #3a3a3a;
    --ink-soft: #4a4a4a;
    --teal: #1d6f86;
    --mark: #2b2524;
  }
  html, body {
    margin: 0;
    padding: 0;
    width: 1200px;
    height: 514px;
    overflow: hidden;
    background: var(--page);
  }
  body {
    position: relative;
    font-family: "Belleza", "Optima", sans-serif;
    color: var(--ink);
  }
  .card {
    position: absolute;
    top: 80px;
    width: 522px;
    height: 349px;
    background: var(--card);
    box-sizing: border-box;
    border: 1px solid var(--card-edge);
    overflow: hidden;
  }

  /* Front */
  .card--front { left: 73px; }
  .front-band {
    position: absolute;
    top: 0;
    bottom: 0;
    width: 92px;
  }
  .front-band--blue {
    left: 0;
    background: radial-gradient(ellipse 70% 60% at 50% 50%, var(--blue-light) 0%, var(--blue) 100%);
  }
  .front-band--orange {
    right: 0;
    width: 91px;
    background: radial-gradient(ellipse 70% 60% at 50% 50%, var(--orange-light) 0%, var(--orange) 100%);
  }
  .front-brand {
    position: absolute;
    left: 130px;
    top: 128px;
    display: flex;
    align-items: center;
    gap: 12px;
  }
  .brand-square {
    width: 83px;
    height: 83px;
    border-radius: 14px;
    background: var(--mark);
  }
  .front-brand .brand-name {
    font-family: "Questrial", "Century Gothic", sans-serif;
    font-size: 42px;
    color: var(--ink-soft);
  }
  .front-web {
    position: absolute;
    left: 92px;
    right: 91px;
    top: 316px;
    text-align: center;
    font-size: 14px;
    letter-spacing: 2.4px;
    color: var(--ink);
  }

  /* Back */
  .card--back { left: 646px; }
  .back-top-bar {
    position: absolute;
    left: 0; right: 0; top: 0;
    height: 6px;
    background: var(--orange);
  }
  .back-left-bar {
    position: absolute;
    left: 0; top: 6px; bottom: 0;
    width: 5px;
    background: var(--blue);
  }
  .back-corner {
    position: absolute;
    right: 0; bottom: 0;
    width: 22px; height: 22px;
  }
  .back-brand {
    position: absolute;
    left: 19px;
    top: 18px;
    display: flex;
    align-items: center;
    gap: 6px;
  }
  .back-brand .brand-square {
    width: 38px;
    height: 38px;
    border-radius: 7px;
  }
  .back-brand .brand-name {
    font-family: "Questrial", "Century Gothic", sans-serif;
    font-size: 20px;
    color: var(--ink-soft);
  }
  .person {
    position: absolute;
    right: 25px;
    top: 27px;
    text-align: right;
    color: var(--teal);
    line-height: 1.05;
  }
  .person-name { font-size: 22px; }
  .person-role { font-size: 19px; }
  .services {
    position: absolute;
    inset: 0;
    width: 100%;
    height: 100%;
  }
  .services text {
    font-family: "Belleza", "Optima", sans-serif;
    font-size: 9.5px;
    letter-spacing: 1.2px;
    fill: var(--teal);
    opacity: 0.75;
  }
  .address {
    position: absolute;
    left: 0; right: 0;
    top: 141px;
    text-align: center;
    font-size: 16.5px;
    line-height: 20.5px;
    color: var(--ink);
  }
  .contact {
    position: absolute;
    left: 17px;
    top: 299px;
    font-size: 16.5px;
    line-height: 21px;
    color: var(--ink);
  }
</style>
</head>
<body>
  <section class="card card--front" aria-label="Card front">
    <div class="front-band front-band--blue"></div>
    <div class="front-band front-band--orange"></div>
    <div class="front-brand">
      <div class="brand-square"></div>
      <span class="brand-name">Vorbelt</span>
    </div>
    <div class="front-web">WWW.VORBELT.COM</div>
  </section>

  <section class="card card--back" aria-label="Card back">
    <div class="back-top-bar"></div>
    <div class="back-left-bar"></div>
    <svg class="back-corner" viewBox="0 0 22 22" aria-hidden="true">
      <rect x="0" y="0" width="22" height="22" fill="var(--blue)"/>
      <rect x="5" y="5" width="17" height="17" fill="var(--orange)"/>
    </svg>
    <div class="back-brand">
      <div class="brand-square"></div>
      <span class="brand-name">Vorbelt</span>
    </div>
    <div class="person">
      <div class="person-name">Marcus Hale</div>
      <div class="person-role">Director</div>
    </div>
    <svg class="services" viewBox="0 0 520 347" aria-label="Services">
      <defs>
        <path id="service-spiral" fill="none"
          d="M 80 272 L 80 108 Q 80 96 92 96 L 436 96 Q 448 96 448 108 L 448 262 Q 448 274 436 274 L 108 274 Q 98 274 98 264 L 98 124 Q 98 114 108 114 L 420 114 Q 430 114 430 124 L 430 246 Q 430 256 420 256 L 130 256"/>
      </defs>
      <text>
        <textPath href="#service-spiral">Project Management · Consulting · Master Systems Integrator · Datacenter · Relocations · Restacks · Project Management · Consulting · Master Systems Integrator · Datacenter · Relocations · Restacks · Project Management · Consulting · Master Systems Integrator</textPath>
      </text>
    </svg>
    <div class="address">
      Vorbelt Pte Ltd<br>
      14 Harbour Quay #05-02<br>
      Linden Point Tower 2<br>
      Singapore&nbsp; 049321
    </div>
    <div class="contact">
      Telephone: +65 8476 2153<br>
      marcus.hale@vorbelt.com
    </div>
  </section>
</body>
</html>
```